Country House in Italy Needs a Business Card Design

We need a business card design for “Casale del Ruscello”, a modern concept of a Farm Holidays/Country House to be opened in central Italy.
Attached is the company logo you did for us in the past.
Please
- create a double-sided business card design
- on the back I would like to have the logo
- on the front the copy
Copy on card:
o Casale del Ruscello
o Address: Via Fontalba, 14
Cingoli (MC), Italy
o Website: www.casaledelruscello.it
o Email: info@casaledelruscello.it
o my name : Lucilla
o my mobile phone number: +39 347 8124591
In the distribution of information keep in mind the possible inclusion also of a landline telephone number (currently not available / existing).
WE WOULD LIKE TO HAVE A MODERN, PROFFESIONAL, OUT OF THE BOX BUSINESS CARD. BE AS CREATIVE AS YOU WOULD LIKE.

```html
<!DOCTYPE html>
<html lang="it">
<head>
<meta charset="utf-8">
<title>Casale del Ruscello – Business Card</title>
<link rel="stylesheet" href="https://fonts.googleapis.com/css2?family=EB+Garamond:wght@400&display=swap">
<style>
  :root {
    --page-bg: #d9d6d2;
    --orange-light: #f6a23e;
    --orange-mid: #ef8526;
    --orange-deep: #e0621a;
    --brown-light: #8a4a1c;
    --brown-mid: #6e3814;
    --brown-deep: #4e260d;
    --ink-brown: #6b3516;
    --logo-orange: #f3a24c;
    --pattern-dark: #7a3d18;
    --pattern-mid: #a0521f;
  }
  * { box-sizing: border-box; margin: 0; padding: 0; }
  html, body {
    width: 1200px;
    height: 1023px;
    overflow: hidden;
    background: var(--page-bg);
    font-family: "EB Garamond", Georgia, serif;
  }
  .sheet {
    width: 1200px;
    height: 1023px;
    display: flex;
    flex-direction: column;
    align-items: center;
    justify-content: center;
    gap: 52px;
  }
  .card {
    position: relative;
    width: 760px;
    height: 434px;
    border-radius: 4px;
    overflow: hidden;
    box-shadow: 0 6px 18px rgba(0,0,0,0.22);
  }

  /* Front: contact copy */
  .card-front {
    background: linear-gradient(160deg, var(--orange-deep) 0%, var(--orange-mid) 38%, var(--orange-light) 100%);
    color: var(--ink-brown);
  }
  .front-pattern {
    position: absolute;
    left: 0;
    bottom: 0;
    width: 340px;
    height: 300px;
  }
  .front-copy {
    position: absolute;
    right: 70px;
    top: 62px;
    width: 380px;
  }
  .person-name {
    font-size: 34px;
    line-height: 1.1;
    margin-bottom: 8px;
  }
  .contact-line {
    font-size: 21px;
    line-height: 1.32;
  }
  .company {
    margin-top: 42px;
  }
  .company-name {
    font-size: 34px;
    line-height: 1.1;
    margin-bottom: 8px;
  }
  .address-line {
    font-size: 21px;
    line-height: 1.32;
  }

  /* Back: name mark */
  .card-back {
    background: radial-gradient(ellipse at 45% 40%, var(--brown-light) 0%, var(--brown-mid) 55%, var(--brown-deep) 100%);
    display: flex;
    align-items: center;
    justify-content: center;
  }
  .brand {
    display: flex;
    align-items: center;
    gap: 28px;
    color: var(--logo-orange);
  }
  .brand-dot {
    width: 120px;
    height: 120px;
    border-radius: 50%;
    background: var(--logo-orange);
  }
  .brand-name {
    font-size: 58px;
    line-height: 1;
    letter-spacing: 0.5px;
  }
</style>
</head>
<body>
<main class="sheet">

  <section class="card card-front" aria-label="Front of business card">
    <svg class="front-pattern" viewBox="0 0 340 300" role="img" aria-label="Decorative radial mosaic pattern in dark brown tones">
      <defs>
        <radialGradient id="mosaicTone" cx="0.45" cy="1" r="1">
          <stop offset="0" stop-color="var(--pattern-dark)"/>
          <stop offset="1" stop-color="var(--pattern-mid)" stop-opacity="0.85"/>
        </radialGradient>
      </defs>
      <path d="M0 300 L0 150 Q20 20 160 10 Q320 20 340 300 Z" fill="url(#mosaicTone)"/>
    </svg>

    <div class="front-copy">
      <p class="person-name">Lucilla</p>
      <p class="contact-line">+39 347 8124591</p>
      <p class="contact-line">info@casaledelruscello.it</p>
      <p class="contact-line">www.casaledelruscello.it</p>

      <div class="company">
        <p class="company-name">Casale del Ruscello</p>
        <p class="address-line">Via Fontalba, 14 Cingoli</p>
        <p class="address-line">(MC), Italy</p>
      </div>
    </div>
  </section>

  <section class="card card-back" aria-label="Back of business card">
    <div class="brand">
      <span class="brand-dot" aria-hidden="true"></span>
      <span class="brand-name">Casale del Ruscello</span>
    </div>
  </section>

</main>
</body>
</html>
```